" ATENDEMOS CLIENTES DE BALCÃO PARA VENDA DE PEÇAS E PNEUS DA LINHA LEVE + CAMIONETES NACIONAIS E IMPORTADOS. CONTAMOS COM UM CENTRO AUTOMOTIVO DE GRANDE PORTE PARA EXECUTAR SERVIÇOS MECÂNICOS DE REVISÃO E MANUTENÇÃO CORRETIVA E PREVENTIVA ( ALINHAMENTO, BALANCEAMENTO, MONTAGEM DE PNEUS, SUSPENSÃO, FREIOS, CAMBIO MANUAL E AUTOMATIZADO, INJEÇÃO ELETRÔNICA, REPARO DE MOTOR E CABEÇOTES, SISTEMA DE DIREÇÃO ). "

```html
<!DOCTYPE html>
<html lang="pt-BR">
<head>
<meta charset="utf-8">
<title>Assinatura de e-mail</title>
<link rel="stylesheet" href="https://fonts.googleapis.com/css2?family=Roboto:wght@400;500;700&display=swap">
<style>
  :root {
    --page: #eceef0;
    --navy: #15212b;
    --white: #ffffff;
    --red: #d9161c;
    --red-dark: #b50f14;
    --ink: #1c1f22;
    --muted: #6b6f73;
  }
  * { margin: 0; padding: 0; box-sizing: border-box; }
  html, body {
    width: 1200px;
    height: 1200px;
    overflow: hidden;
    background: var(--page);
    font-family: "Roboto", Arial, sans-serif;
  }
  .signature {
    position: absolute;
    left: 60px;
    top: 455px;
    width: 1080px;
    height: 290px;
    background: var(--white);
    border-radius: 14px 0 0 14px;
    overflow: hidden;
    box-shadow: 0 2px 10px rgba(0,0,0,0.06);
  }
  .brand-panel {
    position: absolute;
    left: 0; top: 0;
    width: 390px;
    height: 100%;
    background: var(--navy);
    display: flex;
    align-items: center;
    justify-content: center;
    gap: 14px;
  }
  .brand-dot {
    width: 18px; height: 18px;
    border-radius: 50%;
    background: var(--red);
  }
  .brand-name {
    color: var(--white);
    font-weight: 700;
    font-size: 50px;
    letter-spacing: 1px;
  }
  .person {
    position: absolute;
    left: 438px;
    top: 116px;
  }
  .person-name {
    color: var(--red);
    font-size: 31px;
    font-weight: 400;
    letter-spacing: 0.5px;
  }
  .person-role {
    color: var(--muted);
    font-size: 16px;
    margin-top: 4px;
    letter-spacing: 0.5px;
  }
  .contacts {
    position: absolute;
    right: 62px;
    top: 58px;
    list-style: none;
  }
  .contact {
    display: flex;
    align-items: center;
    justify-content: flex-end;
    gap: 26px;
    height: 45px;
    font-size: 23px;
    color: var(--ink);
  }
  .contact svg { width: 20px; height: 22px; fill: var(--red); flex: none; }
  .base-band {
    position: absolute;
    left: 390px;
    bottom: 0;
    width: 690px;
    height: 26px;
  }
</style>
</head>
<body>
  <div class="signature">
    <div class="brand-panel">
      <span class="brand-dot"></span>
      <span class="brand-name">TORKAR</span>
    </div>

    <div class="person">
      <p class="person-name">NOME SOBRENOME</p>
      <p class="person-role">CARGO</p>
    </div>

    <ul class="contacts">
      <li class="contact">nome@empresa.com.br
        <svg viewBox="0 0 20 22"><path d="M1 5h18v12H1z M1 5l9 7 9-7" /><path d="M2 6l8 6 8-6v-0.5H2z" fill="#fff"/></svg>
      </li>
      <li class="contact">99 9999-0000
        <svg viewBox="0 0 20 22"><path d="M4 1h12v20H4zM6.5 3.5v13h7v-13z"/></svg>
      </li>
      <li class="contact">99 99999-9999
        <svg viewBox="0 0 20 22"><path d="M4 1h12v20H4zM6.5 3.5v13h7v-13z"/></svg>
      </li>
      <li class="contact">Rua do Projeto, 999
        <svg viewBox="0 0 20 22"><path d="M10 1a7 7 0 0 0-7 7c0 5 7 13 7 13s7-8 7-13a7 7 0 0 0-7-7zm0 4.5a2.5 2.5 0 1 1 0 5 2.5 2.5 0 0 1 0-5z"/></svg>
      </li>
    </ul>

    <svg class="base-band" viewBox="0 0 690 26" preserveAspectRatio="none">
      <rect x="0" y="20" width="690" height="6" fill="var(--red-dark)"/>
      <path d="M260 26 L300 6 Q305 4 312 4 L690 4 L690 26 Z" fill="var(--red)"/>
    </svg>
  </div>
</body>
</html>
```